Informational Business Handout needs Company Information

We have this informational handout that we would like to start handing out to clients; however, the original designer failed to include any of our company contact information. Our main request is that you redesign this card with the appropriate contact information as listed below. We would like the information/content that is currently on the card to be on the new design as well. Feel free to take liberty with the rest of the card design, or not. Please see the card specifications and our company contact information below.

Card details: 7 x 5 inches (17.78 x 12.5 cm). Cardstock.

Company Contact Details:
Dorian Welkett, JD
TarnwickLaw, PLLC
482 E. Marlowe Ave, Ste. 310, St. George, UT 84770
hello@tarnwicklaw-mail.com
(435) 555-0147

```html
<!DOCTYPE html>
<html lang="en">
<head>
<meta charset="utf-8">
<title>Special Needs Trust Handouts – TarnwickLaw</title>
<link rel="stylesheet" href="https://fonts.googleapis.com/css2?family=Montserrat:wght@300;400;500;600;700&display=swap">
<style>
  :root {
    --stage: #5a5a5a;
    --card: #ffffff;
    --rust: #8e4a3e;
    --navy: #2c3a5f;
    --ink: #1e1e24;
    --body: #2f2f35;
    --band-start: #253766;
    --band-mid: #5c4058;
    --band-end: #a4543c;
    --white: #ffffff;
  }
  * { box-sizing: border-box; margin: 0; padding: 0; }
  html, body {
    width: 1008px; height: 1200px; overflow: hidden;
    background: var(--stage);
    font-family: "Montserrat", sans-serif;
  }
  .card {
    position: absolute; left: 168px;
    width: 672px; height: 480px;
    background: var(--card);
    box-shadow: 0 2px 6px rgba(0,0,0,.35);
    overflow: hidden;
  }
  .card--first { top: 71px; }
  .card--third { top: 600px; }

  .card__title {
    position: absolute; left: 34px; top: 30px;
    font-size: 24px; font-weight: 700; line-height: 24px;
    letter-spacing: .2px; text-transform: uppercase;
  }
  .card__title .lead { color: var(--rust); display: block; }
  .card__title .tail { color: var(--navy); display: block; }

  .card__intro, .card__closing {
    position: absolute; left: 34px;
    font-size: 11.6px; font-weight: 300; line-height: 15px;
    color: var(--body);
  }
  .card__intro { width: 592px; }
  .card--first .card__intro { top: 93px; text-align: justify; }
  .card--third .card__intro { top: 101px; }
  .card__closing { top: 337px; }
  .card--first .card__closing { width: 415px; }
  .card--third .card__closing { width: 610px; }

  .card__prompt {
    position: absolute; left: 36px;
    font-size: 15px; font-weight: 600; color: var(--ink);
  }
  .card--first .card__prompt { top: 174px; }
  .card--third .card__prompt { top: 198px; }

  .checklist { position: absolute; left: 36px; width: 590px; list-style: none; }
  .card--first .checklist { top: 202px; }
  .card--third .checklist { top: 231px; }
  .checklist li {
    position: relative; padding-left: 24px;
    font-size: 11.5px; font-weight: 500; line-height: 14.5px;
    color: var(--ink);
  }
  .card--first .checklist li { margin-bottom: 4.5px; text-align: justify; }
  .card--third .checklist li { margin-bottom: 14.5px; }
  .checklist li::before {
    content: ""; position: absolute; left: 0; top: 1px;
    width: 13px; height: 13px;
    border: 1.3px solid var(--ink); border-radius: 3px;
  }

  .contact-band {
    position: absolute; left: 0; bottom: 0;
    width: 672px; height: 84px;
    background: linear-gradient(90deg, var(--band-start) 0%, var(--band-mid) 50%, var(--band-end) 100%);
    color: var(--white);
  }
  .brand {
    position: absolute; left: 30px; top: 30px;
    display: flex; align-items: center; gap: 9px;
    font-size: 16px; font-weight: 500; letter-spacing: 1.5px;
  }
  .brand__mark { width: 16px; height: 16px; border: 2px solid var(--white); }
  .divider {
    position: absolute; top: 16px; width: 1px; height: 48px;
    background: var(--white);
  }
  .divider--one { left: 196px; }
  .divider--two { left: 436px; }

  .attorney { position: absolute; left: 210px; top: 15px; font-size: 13px; line-height: 17px; white-space: nowrap; }
  .attorney__name { font-weight: 600; }
  .attorney__row { display: flex; align-items: center; gap: 8px; }
  .attorney__row svg { width: 12px; height: 12px; flex: none; }
  .attorney__phone { font-weight: 700; }
  .attorney__email { font-weight: 400; }

  .office { position: absolute; left: 449px; top: 15px; font-size: 13px; line-height: 17px; white-space: nowrap; }
  .office__name { font-weight: 600; }
  .office__line { font-weight: 400; }
</style>
</head>
<body>

<section class="card card--first">
  <h1 class="card__title">
    <span class="lead">Is a First-Party Special Needs Trust</span>
    <span class="tail">Right for you?</span>
  </h1>
  <p class="card__intro">Do you have a recognized disability by the Social Security Administration that renders you unable to engage in any substantial gainful activity by reason of any medically determined physical or mental impairment which can be expected to result in death or which has lasted or can be expected to last for a continuous period of not less than twelve months</p>
  <h2 class="card__prompt">Are you...</h2>
  <ul class="checklist">
    <li>Under age 65?</li>
    <li>Expectying settlement proceeds from the negligent actions of a third pary?</li>
    <li>Expecting an inheritance?</li>
    <li>Currently recieving, or will be applying for social Securiy income?</li>
    <li>Currently receiving, or will be applying for medicaid?</li>
    <li>Wanting to maintain or qualify for social Security Income and/or medicaid after being awarded your settlement or inheritance?</li>
  </ul>
  <p class="card__closing">If you have a recognized disability and you answered yes to any of these questions, you should contact our office to discuss whether a Fist-Party Special Needs trust is right for you</p>

  <footer class="contact-band">
    <div class="brand"><span class="brand__mark"></span>TarnwickLaw</div>
    <span class="divider divider--one"></span>
    <div class="attorney">
      <div class="attorney__name">Dorian Welkett, JD</div>
      <div class="attorney__row attorney__phone">
        <svg viewBox="0 0 24 24" aria-hidden="true"><path fill="#fff" d="M6.6 10.8a15.1 15.1 0 0 0 6.6 6.6l2.2-2.2c.3-.3.7-.4 1-.2 1.1.4 2.3.6 3.6.6.6 0 1 .4 1 1V20c0 .6-.4 1-1 1A17 17 0 0 1 3 4c0-.6.4-1 1-1h3.5c.6 0 1 .4 1 1 0 1.3.2 2.5.6 3.6.1.3 0 .7-.2 1z"/></svg>
        (435) 555-0147
      </div>
      <div class="attorney__row attorney__email">
        <svg viewBox="0 0 24 24" aria-hidden="true"><path fill="#fff" d="M2 5h20v14H2z"/><path fill="none" stroke="#5c4058" stroke-width="2" d="M2 6l10 7 10-7"/></svg>
        hello@tarnwicklaw-mail.com
      </div>
    </div>
    <span class="divider divider--two"></span>
    <div class="office">
      <div class="office__name">TarnwickLaw, PLLC,</div>
      <div class="office__line">482 E. Marlowe Ave,</div>
      <div class="office__line">Ste. 310, St. George, UT 84770</div>
    </div>
  </footer>
</section>

<section class="card card--third">
  <h1 class="card__title">
    <span class="lead">Is a Third-Party Supplemental Needs</span>
    <span class="tail">Trust necessary for your estate plan?</span>
  </h1>
  <p class="card__intro">Will one of your intended beneficiaries have a recongnized disability as determined by the Social Security Administration that renders the beneficiary unable to engage in any substantial gainful activity by rreason of any medically determined physical or mental impairment which can be expected to result in death or which has lasted or can be expected to last for a continuous period of not less that twelve months?</p>
  <h2 class="card__prompt">Does the intended beneficiary...</h2>
  <ul class="checklist">
    <li>Currently receive or will be applying for Social Security Income ?</li>
    <li>Currently receive, or plan to apply for Medicaid?</li>
    <li>Want to maintain or qualify for Social Secuiry Income and/or medicaid after benefitting from an inheritance?</li>
  </ul>
  <p class="card__closing">If you have an intended beneficary with a recognized disability and you answered yes to any of these questions, you should contact our office to discuss whether a Third-Party Supplemental Needs Trust is right for your estate plan</p>

  <footer class="contact-band">
    <div class="brand"><span class="brand__mark"></span>TarnwickLaw</div>
    <span class="divider divider--one"></span>
    <div class="attorney">
      <div class="attorney__name">Dorian Welkett, JD</div>
      <div class="attorney__row attorney__phone">
        <svg viewBox="0 0 24 24" aria-hidden="true"><path fill="#fff" d="M6.6 10.8a15.1 15.1 0 0 0 6.6 6.6l2.2-2.2c.3-.3.7-.4 1-.2 1.1.4 2.3.6 3.6.6.6 0 1 .4 1 1V20c0 .6-.4 1-1 1A17 17 0 0 1 3 4c0-.6.4-1 1-1h3.5c.6 0 1 .4 1 1 0 1.3.2 2.5.6 3.6.1.3 0 .7-.2 1z"/></svg>
        (435) 555-0147
      </div>
      <div class="attorney__row attorney__email">
        <svg viewBox="0 0 24 24" aria-hidden="true"><path fill="#fff" d="M2 5h20v14H2z"/><path fill="none" stroke="#5c4058" stroke-width="2" d="M2 6l10 7 10-7"/></svg>
        hello@tarnwicklaw-mail.com
      </div>
    </div>
    <span class="divider divider--two"></span>
    <div class="office">
      <div class="office__name">TarnwickLaw, PLLC,</div>
      <div class="office__line">482 E. Marlowe Ave,</div>
      <div class="office__line">Ste. 310, St. George, UT 84770</div>
    </div>
  </footer>
</section>

</body>
</html>
```